Brennock Spa

We are a large Miami Beach spa and salon. I am still building our website but you can use it as a resource to gain a better understanding of who we are ....www.halvorwellness.example.

We offer a comprehensive list of services in hair, nails, massage, skin care, tanning, spray tanning and waxing and we offer high quality products for skin care, tanning and hair. We are open 7 days.

We would like to see a clean and simple menu that looks a lot like the one from "The Spa at Solvara." In particular, we have a copy of a menu from their West Hollywood, CA location that is just beautiful. In the uploaded content you will see a sampling of that menu. We would like to see greys, blacks, silvers, whites and warm colors like reds and oranges. We specifically attempt to remain gender neutral so that we don't attract only girls (with pink colors and flowers etc). The final design should convey a simple, clean, friendly environment and the final product should be sized such that it is 1.) portable and 2.) inexpensive to print. We will be running thousands of these at a time so cost of printing is a consideration.

The booklet consists of two parts: one part is the standard menu with descriptions of services and products and photos etc (think of this as the sales piece that convinces a potential customer to visit) and will be stapled together like you would expect a small menu to be and should resemble the Solvara menu. The prices should not be included in this part of the booklet that will be printed and stapled. The other part is a single insert and is removable and replaceable. I want this removable insert placed in the last page of the book in a folder pocket or something else that you can think of so that when it's time to change prices here that I am not throwing away all of the booklets....I am only replacing the inserts at the end of the menu booklet. Please design this single page insert so that should a customer remove it from the booklet and keep it, that it stands alone with our name, logo, website and phone number. This page can and probably will have to be 2 sided.

At the back of the booklet, I also want the polices to be printed in one page (think fine print in any sort of business dealing.)

With regard to the look and feel slider of economical v upmarket...we definitely want to convey we deliver upmarket services at reasonable prices. Think, world class services and products at reasonable, everyday prices.

With regard to the uploaded files:
I uploaded both EPS and TIF formats. The colors in those files are not the palette we want at all. The colors we want use for the circular logo must match the standard colors as depicted in the uploaded file "Brennocktanrooms"

Target Market(s)

The target market is the average 20-35 year old in Miami Beach that cares about their appearance. The range of clientele is quite diverse.

Industry/Entity Type

Environment

Requirements
Must have
• It must have elegant and simple photographs that relate to the services being offered. We are selling a service set and an environment...so this menu should be reflect that goal. The logo should be repeated often throughout the book but in subtle ways.

Stock photos are fine as long as they don't seem obviously stock.

Should not have
• Nothing buddha like. Nothing themed. It should be all inclusive and not seek to identify with any particular group or gender.

Nothing that fits the stereotype of "Miami Beach." We want to represent ourselves in the same category as the best spas in the world because we moving everything we do in that direction. Think class!

```html
<!DOCTYPE html>
<html lang="en">
<head>
<meta charset="utf-8">
<title>Brennock Spa – Massage Menu Spread</title>
<link rel="stylesheet" href="https://fonts.googleapis.com/css2?family=Source+Sans+3:wght@300;400;600&display=swap">
<style>
  :root {
    --page-bg: #ffffff;
    --spa-red: #da4a55;
    --spa-red-deep: #c21f36;
    --spa-red-mist: #c98a8c;
    --photo-dark: #2e1c14;
    --photo-warm: #7b3c22;
    --photo-amber: #a4542c;
    --photo-bedding: #c8424f;
    --band-white: rgba(255, 255, 255, 0.58);
    --frame-line: rgba(240, 225, 205, 0.75);
    --title-grey: #555459;
    --body-dark: #1e1e1e;
    --text-light: #ffffff;
    --brand-gold: #c9a46a;
  }
  * { margin: 0; padding: 0; box-sizing: border-box; }
  html, body {
    width: 1200px; height: 600px; overflow: hidden;
    background: var(--page-bg);
  }
  .spread {
    position: relative; width: 1200px; height: 600px; overflow: hidden;
    font-family: "Source Sans 3", "Helvetica Neue", Arial, sans-serif;
  }
  .spread__art { position: absolute; inset: 0; }

  .section-title {
    position: absolute; left: 46px; top: 470px;
    font-size: 44px; font-weight: 300; letter-spacing: 0.2em;
    color: var(--title-grey); line-height: 1;
  }
  .section-intro {
    position: absolute; left: 320px; top: 465px; width: 268px;
    font-size: 8px; font-weight: 600; letter-spacing: 0.09em;
    line-height: 10.5px; color: var(--body-dark);
  }

  .service { position: absolute; left: 704px; top: 64px; width: 440px; color: var(--text-light); }
  .service__head, .service__row {
    display: grid; grid-template-columns: 262px 75px 1fr; align-items: baseline;
  }
  .service__head { font-size: 12px; font-weight: 400; }
  .service__name { text-transform: uppercase; }
  .service__desc {
    margin-top: 16px; width: 420px;
    font-size: 10px; line-height: 16.7px; font-weight: 400;
  }
  .service__row { margin-top: 17px; font-size: 9.5px; }

  .brand {
    position: absolute; left: 1040px; top: 548px; width: 110px;
    display: flex; flex-direction: column; align-items: center; gap: 6px;
  }
  .brand__mark {
    width: 26px; height: 26px; border-radius: 50%;
    border: 1.5px solid var(--brand-gold);
  }
  .brand__name {
    font-size: 13px; font-weight: 400; letter-spacing: 0.12em;
    color: var(--brand-gold); text-transform: uppercase; white-space: nowrap;
  }
</style>
</head>
<body>
<main class="spread">
  <svg class="spread__art" width="1200" height="600" viewBox="0 0 1200 600" aria-hidden="false">
    <defs>
      <linearGradient id="photoTone" x1="0" y1="0" x2="0.3" y2="1">
        <stop offset="0" stop-color="var(--photo-dark)"/>
        <stop offset="0.35" stop-color="var(--photo-warm)"/>
        <stop offset="0.6" stop-color="var(--photo-amber)"/>
        <stop offset="1" stop-color="var(--photo-bedding)"/>
      </linearGradient>
      <linearGradient id="panelTone" x1="0" y1="0" x2="1" y2="1">
        <stop offset="0" stop-color="var(--spa-red)"/>
        <stop offset="0.62" stop-color="var(--spa-red)"/>
        <stop offset="0.8" stop-color="var(--spa-red-mist)"/>
        <stop offset="1" stop-color="var(--spa-red-deep)"/>
      </linearGradient>
    </defs>
    <rect class="feature-photo" x="0" y="0" width="670" height="600" fill="url(#photoTone)"
          role="img" aria-label="Photo: a therapist guiding a fully clothed client through an assisted Thai massage stretch in a warmly lit treatment room"/>
    <rect class="title-band" x="0" y="432" width="670" height="108" fill="var(--band-white)"/>
    <path class="service-panel" d="M665,0 H1200 V600 H548 C612,600 665,540 665,427 Z" fill="url(#panelTone)"/>
    <rect class="page-frame" x="19" y="18" width="1162" height="565" fill="none" stroke="var(--frame-line)" stroke-width="1.5"/>
  </svg>

  <h1 class="section-title">MASSAGE</h1>
  <p class="section-intro">Tina, conves conduc ta Simis sus, portis, eo esilicie mei potidees? Arbessules curnihil hacchil lesigiti clum et vit; nicaella ponloctur. Imo in tam poste, quam iam re confit. Ego publicesse te mac tenihil</p>

  <section class="service">
    <div class="service__head">
      <h2 class="service__name" style="font-size:inherit;font-weight:inherit">Thai Massage</h2>
      <span class="service__col">Residents</span>
      <span class="service__col">Hotel Guests</span>
    </div>
    <p class="service__desc">Unlike traditional massage in which you are expected to shed some clothing, Thai massage is performed with the recipient fully clothed. You are instructed to lie on a padded mat on the floor. During therapy, the practitioner may rock you, perform rhythmic muscle compression, assisted yoga positions, and stretches. Practitioners work along your energy meridians and make use of their knees, forearms, elbows, palms, and thumbs to remove knots and relieve muscle tension. The therapy can last anywhere from 30 to 90 minutes. Search for therapists and pricing in your area by visiting the Coastal Massage Therapy Guild.</p>
    <div class="service__row">
      <span>The Thai Session (45-60 Minutes)</span>
      <span>$79.00</span>
      <span>$90.00</span>
    </div>
  </section>

  <div class="brand">
    <span class="brand__mark"></span>
    <span class="brand__name">Brennock Spa</span>
  </div>
</main>
</body>
</html>
```